依頼詳細
会社の名刺作成をお願いします。シンプルなデザインでおねがいします。
ヨコ型の名刺でお願いします
記載項目
TOLIQ VANTE の社名で添付に字体とロゴがあります。
名前、固定電話、携帯電話、メールアドレスの一般的な記載です。字体は、添付のTOLIQ VANTE にあうものでお願いします。
希望イメージ
シンプル 複雑
単色 カラフル
暗い 明るい
日常 高級
遊び心 厳粛
未来的 伝統的
女性的 男性的
希望する色
赤系、グレー系
納品ファイル
補足説明
■ 選んだ理由

きちんと主張してインパクトのある模様です。

■ 提案者全員のお礼・コメント

みなさまありがとうございます。今後もよろしくお願いします

```html
<!DOCTYPE html>
<html lang="ja">
<head>
<meta charset="utf-8">
<title>TOLIQ VANTE 名刺</title>
<link rel="stylesheet" href="https://fonts.googleapis.com/css2?family=Noto+Sans+JP:wght@400;700&family=Montserrat:wght@500&display=swap">
<style>
  :root {
    --backdrop: #7b8090;
    --card: #ffffff;
    --ink: #1a1a1a;
    --brand-red: #a8242a;
    --photo-light: #d9e8ee;
    --photo-mid: #7fa9b8;
    --photo-deep: #3f6f82;
  }
  * { margin: 0; padding: 0; box-sizing: border-box; }
  html, body { width: 848px; height: 1200px; overflow: hidden; }
  body {
    background: var(--backdrop);
    position: relative;
    font-family: "Noto Sans JP", sans-serif;
    color: var(--ink);
  }
  .card { position: absolute; background: var(--card); overflow: hidden; }
  .card--front { left: 93px; top: 40px; width: 643px; height: 390px; }
  .card--back { left: 207px; top: 467px; width: 435px; height: 685px; }

  .brand { position: absolute; display: flex; align-items: center; }
  .brand__mark { background: var(--brand-red); }
  .brand__name {
    font-family: "Montserrat", sans-serif;
    font-weight: 500;
    color: var(--ink);
    letter-spacing: 0.02em;
  }
  .card--front .brand { left: 36px; top: 30px; gap: 12px; }
  .card--front .brand__mark { width: 26px; height: 26px; }
  .card--front .brand__name { font-size: 27px; }

  .photo {
    position: absolute; right: 0; top: 0; width: 227px; height: 220px;
    background:
      linear-gradient(90deg, var(--card) 0%, rgba(255,255,255,0) 35%),
      linear-gradient(160deg, var(--photo-light) 0%, var(--photo-mid) 55%, var(--photo-deep) 100%);
  }

  .person-name {
    position: absolute; left: 118px; top: 150px;
    font-size: 44px; font-weight: 700; letter-spacing: 0.04em;
  }
  .contact {
    position: absolute; left: 52px; top: 268px;
    list-style: none; font-size: 17px; line-height: 1.62;
  }

  .card--back .brand {
    left: 0; right: 0; top: 235px;
    flex-direction: column; gap: 52px;
  }
  .card--back .brand__mark { width: 130px; height: 130px; }
  .card--back .brand__name { font-size: 32px; }
</style>
</head>
<body>
  <section class="card card--front">
    <div class="brand">
      <span class="brand__mark"></span>
      <span class="brand__name">TOLIQ VANTE</span>
    </div>
    <div class="photo" role="img" aria-label="作業中の技術者の写真"></div>
    <h1 class="person-name">山田 太郎</h1>
    <ul class="contact">
      <li>TEL 00-0000-0000</li>
      <li>携帯 00-0000-0000</li>
      <li>Email ○○@○○.com</li>
    </ul>
  </section>

  <section class="card card--back">
    <div class="brand">
      <span class="brand__mark"></span>
      <span class="brand__name">TOLIQ VANTE</span>
    </div>
  </section>
</body>
</html>
```